CEO of company needs clear business card that stands out from the rest

I need a clear business card (standard credit card size) for the CEO/Founder of our company...Brightfield Counseling. We would like to see designs that use our logo colors, which are khaki, chocolate brown, and gray. The card should be an edgy design, maybe where half the card is transparent with curves on the card, or a textured card where the logo is transparent, I don't care much for white cards. The final design should communicate a funky, edgy, and modern look, as well as stand out to have the "WOW" factor. The information we need on the card would be Name, Title, Toll free number, Phone Number, address, email address, and website.

*PLEASE SEND FRONT AND BACK OF CARDS

Card is two sided front and back please give us your front and back designs

The card should be an edgy design, maybe where half the card is transparent with curves on the card, or a textured card where the logo is transparent, I don't care much for white cards. The final design should communicate a funky, edgy, and modern look, as well as stand out to have the "WOW" factor.

Please follow these guidelines for the card

SPECS (card):

2.125 (h) x 3.375 (w) card size after cut

2.375 (h) x 3.625 (w) card with bleed

300 dpi

cmyk

1/8 bleed

allow 1/8 border for live area

I will also attached the pdf for the information listed above which includes a diagram of the card

 

All the cards need to have rounded edges

I just updated a card as an example of how you can use different fonts on a single business card, look how the name is written in script, so what I am saying is make this a card you will be proud to design and put it in your portfolio 

Reason: this race is really close and I am working with 2 designers to fine tune their designs and the weekend is slowing us down

• Our Logo
MUST HAVE PARTS OF CARD THAT ARE TRANSPARENT. See ideas that are attached.
Card is two sided front and back
• The final design should communicate a funky, edgy, and modern look, as well as stand out to have the "WOW" factor. The information we need on the card would be Name, Title, Toll free number, Phone Number, address, email address, and website.

```html
<!DOCTYPE html>
<html lang="en">
<head>
<meta charset="utf-8">
<title>Brightfield Counseling – Business Card</title>
<link href="https://fonts.googleapis.com/css2?family=Arimo:wght@400;700&family=Pinyon+Script&display=swap" rel="stylesheet">
<style>
  :root {
    --backdrop: #2b2622;
    --card-white: #ffffff;
    --panel-grey-top: #cdcdcd;
    --panel-grey-bottom: #e2e2e2;
    --soft-grey: #a8a8a8;
    --chocolate: #7a3512;
    --chocolate-light: #a24d1f;
    --ink: #1e1e1e;
    --ink-soft: #3a3a3a;
  }
  html, body {
    margin: 0;
    padding: 0;
    width: 1200px;
    height: 900px;
    overflow: hidden;
    background: var(--backdrop);
    font-family: "Arimo", Arial, sans-serif;
  }
  .canvas {
    position: relative;
    width: 1200px;
    height: 900px;
  }
  .card {
    position: absolute;
    left: 330px;
    width: 540px;
    height: 340px;
    border-radius: 22px;
    overflow: hidden;
    background: var(--card-white);
    box-shadow: 0 10px 30px rgba(0,0,0,0.45);
  }
  .card--front { top: 70px; }
  .card--back { top: 490px; }

  .front-art {
    position: absolute;
    inset: 0;
    background:
      linear-gradient(100deg,
        var(--soft-grey) 0%,
        #d4d4d4 22%,
        var(--card-white) 40%,
        var(--card-white) 62%,
        #d9a07e 78%,
        var(--chocolate-light) 90%,
        var(--chocolate) 100%);
  }

  .back-panel {
    position: absolute;
    left: 10px;
    top: 10px;
    right: 10px;
    height: 236px;
    border-radius: 14px 14px 0 0;
    background: linear-gradient(180deg, var(--panel-grey-top), var(--panel-grey-bottom));
  }
  .back-rule {
    position: absolute;
    left: 10px;
    right: 10px;
    top: 246px;
    height: 3px;
    background: var(--chocolate);
  }

  .brand {
    position: absolute;
    display: flex;
    align-items: center;
    gap: 8px;
  }
  .brand__dot {
    width: 20px;
    height: 20px;
    border-radius: 50%;
    background: var(--chocolate);
    flex: none;
  }
  .brand__name {
    font-family: "Arimo", Arial, sans-serif;
    font-weight: 700;
    color: var(--chocolate);
    white-space: nowrap;
  }
  .card--front .brand { left: 50%; top: 158px; transform: translateX(-50%); }
  .card--front .brand__name { font-size: 20px; }
  .card--back .brand { left: 26px; top: 276px; }
  .card--back .brand__name { font-size: 22px; }

  .contact {
    position: absolute;
    right: 34px;
    top: 28px;
    text-align: right;
    color: var(--ink);
    font-size: 11.5px;
    line-height: 14px;
  }
  .contact p { margin: 0 0 6px; }
  .contact__label { font-weight: 700; }
  .person {
    position: absolute;
    right: 34px;
    top: 180px;
    text-align: right;
  }
  .person__name {
    margin: 0;
    font-family: "Pinyon Script", cursive;
    font-size: 24px;
    line-height: 26px;
    color: var(--ink);
  }
  .person__title {
    margin: 2px 0 0;
    font-size: 12px;
    color: var(--ink-soft);
  }
</style>
</head>
<body>
<main class="canvas">

  <section class="card card--front" aria-label="Card front">
    <div class="front-art" role="img" aria-label="Decorative sweeping bands in grey and chocolate brown framing the company name"></div>
    <div class="brand">
      <span class="brand__dot"></span>
      <span class="brand__name">Brightfield Counseling</span>
    </div>
  </section>

  <section class="card card--back" aria-label="Card back">
    <div class="back-panel"></div>
    <div class="back-rule"></div>

    <div class="contact">
      <p>4810 Linden Ridge Dr. N.W. Suite 210<br>Marietta GA 30060</p>
      <p>
        <span class="contact__label">TOLL FREE #:</span> 1.855.555.0148<br>
        <span class="contact__label">TEL:</span> 404.555.0172<br>
        <span class="contact__label">FEX:</span> 678.555.0139
      </p>
      <p>awhitlock@brightfieldcounseling.com<br>www.brightfieldcounseling.com</p>
    </div>

    <div class="person">
      <p class="person__name">Adrian Whitlock</p>
      <p class="person__title">Founder / CEO</p>
    </div>

    <div class="brand">
      <span class="brand__dot"></span>
      <span class="brand__name">Brightfield Counseling</span>
    </div>
  </section>

</main>
</body>
</html>
```